Poster for Kirtan Music Event

Design (3) 24" x 36" Posters

I have provided a sample a friend did in Australia: ( Picture No. 4 )

Use all the text on sample poster except the replacement changes below.

Replace with the following text as this is for different location:
Replacement Text:

Every Friday Night 7:00pm-8:30pm
Nohea Breath & Movement Loft
752 Wenmore St Paia

Free Kirtan Experience! or Free Event
Madhava Vani Prabhu & Friends

Optional Text:

A evening of music, singing of spiritual mantras, and refreshments

Bring flowers, musical instruments, friends, or just come with an open heart.

Meditate on transcendental sounds that provide rest for the mind & heart"

An evening of music & singing of sacred mantra's

```html
<!DOCTYPE html>
<html lang="en">
<head>
<meta charset="utf-8">
<title>Kirtan Experience</title>
<link rel="stylesheet" href="https://fonts.googleapis.com/css2?family=Yatra+One&family=Rouge+Script&family=Noto+Serif+Devanagari:wght@500&display=swap">
<style>
  :root {
    --green-deep: #2f6f24;
    --green-mid: #4a9236;
    --green-light: #5fa646;
    --orange: #f0731c;
    --amber: #f5941a;
    --sun: #f2ee2a;
    --ink: #1d1a12;
    --script-red: #b1241b;
    --paper: #f1cf93;
    --paper-edge: #d9b478;
    --brown: #6a2616;
    --photo-frame: #e8d6b0;
  }
  * { margin: 0; padding: 0; box-sizing: border-box; }
  html, body { width: 800px; height: 1200px; overflow: hidden; background: var(--green-deep); }
  .poster {
    position: relative; width: 800px; height: 1200px; overflow: hidden;
    background:
      repeating-linear-gradient(180deg, rgba(255,255,255,0.05) 0 14px, rgba(0,0,0,0.04) 14px 28px),
      radial-gradient(ellipse at 40% 45%, var(--green-light), var(--green-mid) 45%, var(--green-deep) 100%);
  }
  .pattern-area {
    position: absolute; left: 40px; top: 240px; width: 520px; height: 660px; z-index: 0;
    background: radial-gradient(ellipse at center, rgba(192,57,43,0.75), rgba(192,57,43,0.35) 60%, rgba(192,57,43,0) 75%);
  }
  .photo {
    position: absolute; z-index: 1; border: 14px solid var(--photo-frame);
    box-shadow: 3px 4px 8px rgba(0,0,0,0.45);
  }
  .photo-singer { left: 485px; top: 205px; width: 340px; height: 240px; transform: rotate(-9deg);
    background: linear-gradient(135deg, #d9d2c8, #8a5a45 60%, #3b2a24); }
  .photo-harmonium { left: 510px; top: 385px; width: 320px; height: 330px; transform: rotate(5deg);
    background: linear-gradient(160deg, #b98a4a, #e8dcc6 45%, #6b3f22); }
  .photo-chanter { left: 495px; top: 715px; width: 330px; height: 280px; transform: rotate(-9deg);
    background: linear-gradient(135deg, #6e8d5a, #e6b45a 50%, #7a8fa8); }

  .title-main, .title-sub, .keyword, .schedule {
    font-family: "Yatra One", "Trebuchet MS", sans-serif; position: absolute; line-height: 1; white-space: nowrap;
  }
  .title-main, .title-sub, .peace-word, .tagline, .keyword, .invite, .om-sun { z-index: 2; }
  .title-main { left: 38px; top: 4px; font-size: 128px; color: var(--orange); letter-spacing: 22px; }
  .title-sub { left: 150px; top: 176px; font-size: 88px; color: var(--amber); letter-spacing: 3px; }
  .om-sun {
    position: absolute; left: 604px; top: 14px; width: 170px; height: 150px;
    border-radius: 50%; background: radial-gradient(circle, var(--sun) 45%, rgba(242,238,42,0.6) 65%, rgba(242,238,42,0) 72%);
  }
  .peace-word {
    position: absolute; left: 22px; top: 196px; font-family: "Noto Serif Devanagari", serif;
    font-size: 38px; color: var(--ink); line-height: 1;
  }
  .tagline {
    position: absolute; left: 40px; top: 266px; font-family: "Rouge Script", cursive;
    font-size: 62px; font-weight: 700; color: var(--ink); line-height: 62px; white-space: nowrap;
  }
  .keyword { left: 115px; top: 382px; font-size: 62px; color: var(--ink); letter-spacing: 3px; }
  .invite {
    position: absolute; left: 20px; top: 894px; width: 660px; text-align: center;
    font-family: "Rouge Script", cursive; font-size: 50px; font-weight: 700; line-height: 54px;
    color: var(--script-red); white-space: nowrap;
  }
  .details {
    position: absolute; left: 38px; top: 1008px; width: 726px; height: 180px; z-index: 2;
    background: var(--paper); border: 2px solid var(--paper-edge);
  }
  .schedule { left: 0; width: 100%; text-align: center; font-size: 38px; color: var(--brown); letter-spacing: 2px; text-transform: lowercase; }
  .schedule-time { top: 26px; }
  .schedule-venue { top: 76px; font-size: 36px; }
  .schedule-address { top: 126px; font-size: 36px; }
</style>
</head>
<body>
<main class="poster">
  <div class="pattern-area" role="img" aria-label="Red folk motif of peacocks and lotus flowers"></div>

  <div class="photo photo-singer" role="img" aria-label="Photo of a woman singing during kirtan"></div>
  <div class="photo photo-harmonium" role="img" aria-label="Photo of a woman playing harmonium and singing"></div>
  <div class="photo photo-chanter" role="img" aria-label="Photo of a man chanting into a microphone"></div>

  <h1 class="title-main">kirtan</h1>
  <div class="om-sun" role="img" aria-label="Yellow Om emblem inside a radiating sun"></div>
  <p class="peace-word" lang="hi">शान्ति</p>
  <h2 class="title-sub">experience</h2>

  <p class="tagline">An evening of music<br>&amp; singing of sacred</p>
  <p class="keyword">mantra's</p>

  <p class="invite">Free Kirtan Experience<br>with Madhava Vani Prabhu &amp; Friends</p>

  <section class="details">
    <p class="schedule schedule-time">every friday night 7:00pm-8:30pm</p>
    <p class="schedule schedule-venue">Nohea Breath &amp; Movement Loft</p>
    <p class="schedule schedule-address">752 Wenmore St paia</p>
  </section>
</main>
</body>
</html>
```